Halvik Denatl Laboratory nees a window design

We want to make a window cover 8 feet wide and 6 feet tall to advertise our dental lab with all the products we produce<br/>: Digital Cad/Cam<br/>: Implants<br/>: Dentures<br/>: Cast Partials <br/>: Orthodontic appliances<br/><br/> and it has to include a service we provide for a denturist on site by appointment only.<br/><br/>Please use the sample logo below our colours are white backround and blue letters

Font styles to use
Script

Colors
ffffff
0355a3

Requirements
Nice to have
• a picture of a teddy bear on a dental chair, or some dental work particularly bridge work since our moto is Building bridges since 1976
Should not have
• real people

```html
<!DOCTYPE html>
<html lang="en">
<head>
<meta charset="utf-8">
<title>Halvik Denatl Laboratory – Window Cover</title>
<link href="https://fonts.googleapis.com/css2?family=Pinyon+Script&family=Oswald:wght@400;500;600&family=Didact+Gothic&display=swap" rel="stylesheet">
<style>
  :root {
    --white: #ffffff;
    --navy: #0355a3;
    --ink: #0b3f7a;
    --sky: #2a9fd8;
    --light-sky: #35aee0;
    --paper: #f4f6f8;
    --stage: #e6eaee;
  }
  * { margin: 0; padding: 0; box-sizing: border-box; }
  html, body { width: 1200px; height: 807px; overflow: hidden; background: var(--stage); }
  .canvas { position: relative; width: 1200px; height: 807px; }
  .window-cover {
    position: absolute; left: 40px; top: 143px; width: 1120px; height: 520px;
    background: var(--paper); overflow: hidden;
    box-shadow: 0 6px 24px rgba(0,0,0,.12);
  }
  .wave { position: absolute; inset: 0; }
  .brand-mark {
    position: absolute; left: 50px; top: 50px; width: 170px; height: 170px;
    border-radius: 50%; background: var(--light-sky);
  }
  .brand-name {
    position: absolute; left: 240px; top: 40px;
    font-family: "Pinyon Script", cursive; font-size: 84px; color: var(--ink);
    white-space: nowrap;
  }
  .products { position: absolute; left: 330px; top: 175px; font-family: "Oswald", sans-serif; }
  .products-title { font-size: 42px; font-weight: 600; color: var(--ink); letter-spacing: .5px; }
  .products-list { list-style: none; font-size: 29px; font-weight: 500; color: var(--sky); line-height: 1.18; margin-top: 4px; }
  .service { position: absolute; right: 210px; top: 335px; text-align: right; font-family: "Oswald", sans-serif; color: var(--ink); }
  .service-line { font-size: 23px; font-weight: 500; }
  .service-emphasis { font-size: 40px; font-weight: 600; line-height: 1.1; }
  .illustration {
    position: absolute; right: 25px; top: 250px; width: 170px; height: 215px;
    border-radius: 12px;
    background: linear-gradient(160deg, #dfe7ee 0%, #c9d6e2 55%, #f1c24a 100%);
  }
  .web-address {
    position: absolute; left: 30px; top: 420px;
    font-family: "Didact Gothic", sans-serif; font-size: 26px; color: var(--white);
    transform: rotate(5deg); transform-origin: left center;
  }
</style>
</head>
<body>
<main class="canvas">
  <section class="window-cover">
    <svg class="wave" viewBox="0 0 1120 520" preserveAspectRatio="none" aria-hidden="true">
      <path d="M0 330 C 300 420, 650 520, 1120 470 L1120 520 L0 520 Z" fill="var(--light-sky)"/>
      <path d="M0 320 C 280 410, 620 505, 1090 455 C 1060 500, 980 520, 900 520 L0 520 Z" fill="var(--navy)"/>
      <path d="M0 320 C 280 410, 620 505, 1090 455" fill="none" stroke="var(--white)" stroke-width="3" opacity=".6"/>
    </svg>

    <div class="brand-mark"></div>
    <h1 class="brand-name">Halvik Denatl Laboratory</h1>

    <div class="products">
      <h2 class="products-title">PRODUCTS WE PRODUCE</h2>
      <ul class="products-list">
        <li>• DIGITAL CAD/CAM • IMPLANTS • DENTURES</li>
        <li>• CAST PARTIALS • ORTHODONTIC APPLIANCES</li>
      </ul>
    </div>

    <div class="service">
      <p class="service-line">SERVICE WE PROVIDE FOR A DENTURIST ON SITE BY</p>
      <p class="service-emphasis">APPOINTMENT ONLY</p>
    </div>

    <div class="illustration" role="img" aria-label="Illustration of a cheerful character relaxing in a dental chair"></div>

    <p class="web-address">www.halvikdenatllab.com</p>
  </section>
</main>
</body>
</html>
```